Letterhead Design

I have my company logo, slogan, etc. please refer to attachment for your onward design.

An Overview / Background of the Business & Services – Specialised in high-end boutique interior furnishing and fabricate furniture.

The Target Market / Audience you are trying to reach – Global client to US for high-end brand. 90% of our client are from USA.

Design Specifics; any preferences or ideas for Style, Colour, Imagery, etc – No. We have our own logo and slogan, hence would need design of letterhead, business card, envelopes and complimentary slip, if possible, otherwise letterhead will do.

Industry/Entity Type

Boutique

```html
<!DOCTYPE html>
<html lang="en">
<head>
<meta charset="utf-8">
<title>Meridian Crest Interiors – Letterhead</title>
<link href="https://fonts.googleapis.com/css2?family=Didact+Gothic&family=Roboto:wght@400;700&display=swap" rel="stylesheet">
<style>
  :root {
    --backdrop: #ebebeb;
    --paper: #ffffff;
    --brown-dark: #4a3636;
    --brown-tan: #d8bcae;
    --ink: #3a2b2b;
    --sketch-a: #f6f6f6;
    --sketch-b: #ededed;
  }
  html, body {
    margin: 0;
    width: 1200px;
    height: 1192px;
    overflow: hidden;
    background: var(--backdrop);
  }
  .letterhead {
    position: absolute;
    left: 230px;
    top: 58px;
    width: 740px;
    height: 1076px;
    background: var(--paper);
    box-shadow: 0 4px 18px rgba(0,0,0,0.12);
    overflow: hidden;
    font-family: "Roboto", Arial, sans-serif;
    color: var(--ink);
  }
  .brand {
    position: absolute;
    right: 48px;
    top: 52px;
    display: flex;
    align-items: center;
    gap: 10px;
  }
  .brand-square {
    width: 22px;
    height: 22px;
    background: var(--brown-dark);
  }
  .brand-name {
    font-family: "Roboto", Arial, sans-serif;
    font-weight: 700;
    font-size: 20px;
    letter-spacing: 2px;
    color: var(--brown-dark);
  }
  .sketch-area {
    position: absolute;
    left: 0;
    top: 360px;
    width: 100%;
    height: 560px;
    background: radial-gradient(ellipse at 60% 45%, var(--sketch-b) 0%, var(--sketch-a) 55%, var(--paper) 85%);
  }
  .contact {
    position: absolute;
    left: 46px;
    top: 838px;
    display: flex;
    gap: 40px;
    font-size: 12px;
    line-height: 17px;
  }
  .company-name {
    font-weight: 700;
    font-size: 16px;
    margin-bottom: 3px;
  }
  .address-line, .contact-line {
    display: flex;
    align-items: center;
    gap: 6px;
  }
  .address-line .spacer { width: 10px; }
  .contact-lines { padding-top: 36px; }
  .icon { width: 11px; height: 11px; fill: var(--ink); flex: none; }
  .bands {
    position: absolute;
    left: 0;
    bottom: 0;
    width: 100%;
    height: 150px;
  }
</style>
</head>
<body>
  <main class="letterhead">
    <div class="brand">
      <span class="brand-square"></span>
      <span class="brand-name">MERIDIAN CREST</span>
    </div>

    <div class="sketch-area" role="img" aria-label="Faint architectural interior sketch in light grey"></div>

    <section class="contact">
      <div class="address">
        <div class="company-name">Meridian Crest Interiors Pte Ltd</div>
        <div class="address-line">
          <svg class="icon" viewBox="0 0 12 12"><path d="M6 0a4 4 0 0 0-4 4c0 3 4 8 4 8s4-5 4-8a4 4 0 0 0-4-4zm0 5.5A1.5 1.5 0 1 1 6 2.5a1.5 1.5 0 0 1 0 3z"/></svg>
          <span>12 Harbourline Road #05-22</span>
        </div>
        <div class="address-line"><span class="spacer"></span><span>Linden Court Singapore 408812</span></div>
      </div>
      <div class="contact-lines">
        <div class="contact-line">
          <svg class="icon" viewBox="0 0 12 12"><path d="M2.5 0.5l2 2-1 1.5c.6 1.6 1.9 2.9 3.5 3.5l1.5-1 2 2-1.5 2C5 10.5 1.5 7 .5 2z"/></svg>
          <span>+65 6200 4187</span>
        </div>
        <div class="contact-line">
          <svg class="icon" viewBox="0 0 12 12"><path d="M3 0h6v3H3zM1 4h10v5H9v3H3V9H1zm3 3v4h4V7z"/></svg>
          <span>+65 6200 4190</span>
        </div>
        <div class="contact-line">
          <svg class="icon" viewBox="0 0 12 12"><path d="M0 2h12v8H0zm1 1v.5l5 3.5 5-3.5V3z"/></svg>
          <span>hello@meridiancrest.com.sg</span>
        </div>
      </div>
    </section>

    <svg class="bands" viewBox="0 0 740 150" preserveAspectRatio="none" aria-hidden="true">
      <path d="M0 20 C 220 70, 480 95, 740 88 L740 150 L0 150 Z" fill="var(--brown-tan)"/>
      <path d="M0 30 C 250 85, 500 110, 740 110 L740 150 L0 150 Z" fill="var(--paper)"/>
      <path d="M0 40 C 260 95, 500 118, 740 118 L740 150 L0 150 Z" fill="var(--brown-dark)"/>
    </svg>
  </main>
</body>
</html>
```